Design Large Inspirational Artwork with Long Quote

Design a large piece of art with a quote from Marcus Hallwell.

QUOTE
"The thing that's so interesting about being alive is that you're all in. No matter what you do, you're all in. This is gonna kill you, so I think you might as well play the most magnificent game you can while you're waiting. Because, do you have anything better to do? Why not pick the best thing possible that you could do? Because you're more powerful than you think, way more powerful than you think. I mean, God only knows what you are in the final analysis. You're blind to your own weaknesses, but you're also blind to your own strengths. How far could you take that if you stopped wasting time, and if you stopped lying, and if you oriented yourself to the highest possible good that you could conceive of and you committed to that? How much good could you do? Well, I would say: why don't you find out?"

SIZE
A high-resolution print size of 6' wide and 3' tall should provide ample space for both the quote and the accompanying artwork.

TYPOGRAPHY
Choose a bold, clean, and easily readable font for the quote. You could also experiment with different font sizes for certain words or phrases to emphasize their importance within the quote.

COLORS
Since the quote is thought-provoking and reflective, you might want to use a color palette that evokes a sense of introspection and depth. Consider using cool, calming colors like shades of blue, gray, or green. Alternatively, you can use a contrasting color scheme with a light background and dark text to make the quote stand out.

ARTWORK
Select / create / edit background artwork to complement the quote.
While a great design might be minimalistic and/or greyscale, I'd really like to see some full color options. This might be anything from photography or graphics inspired by the ideas in the text, to abstract colors or illustrations that feel like the sentiment expressed.
The art should capture your attention and encourage you to read the text. The art should be visually appealing, both at a distance and up close, regardless of whether the text is read.
Updates

Having trouble confirming the exact print size.

Still looking for printing solution and final size confirmation.

Target Market(s)

Personal, business, office

Industry/Entity Type

None

Font styles to use
Sans Serif
Script

Requirements
Must have
• Entire quote, legible text, modern design, attractive artwork, approx 6ft wide and 3ft tall
Nice to have
• Different font (sizes) for certain words or phrases to emphasize their importance within the quote.

```html
<!DOCTYPE html>
<html lang="en">
<head>
<meta charset="utf-8">
<title>Why Don't You Find Out — Quote Artwork</title>
<link rel="stylesheet" href="https://fonts.googleapis.com/css2?family=Exo+2:ital,wght@0,400;1,500;1,800&display=swap">
<style>
  :root {
    --ink: #141414;
    --accent-red: #e3161d;
    --headline-white: #ffffff;
    --sky-top: #9fb3c8;
    --sky-mid: #e9e7e4;
    --haze: #f3ede4;
    --sun-core: #fff2c4;
    --sun-glow: #f7a142;
    --dusk-orange: #d86a1f;
    --rock-dark: #3a2117;
  }
  html, body {
    margin: 0;
    padding: 0;
    width: 1200px;
    height: 602px;
    overflow: hidden;
    background: #ffffff;
  }
  .artwork {
    position: relative;
    width: 1200px;
    height: 602px;
    overflow: hidden;
    font-family: "Exo 2", sans-serif;
    color: var(--ink);
  }
  .backdrop {
    position: absolute;
    inset: 0;
    background:
      radial-gradient(ellipse 380px 260px at 600px 600px, var(--sun-core) 0%, var(--sun-glow) 40%, rgba(216,106,31,0) 100%),
      radial-gradient(ellipse 420px 380px at 0px 602px, var(--rock-dark) 0%, rgba(58,33,23,0.85) 45%, rgba(58,33,23,0) 100%),
      radial-gradient(ellipse 360px 300px at 1200px 560px, rgba(120,60,30,0.9) 0%, rgba(150,80,40,0.6) 45%, rgba(150,80,40,0) 100%),
      linear-gradient(180deg, var(--sky-top) 0%, var(--sky-mid) 28%, var(--haze) 52%, #f2c58c 72%, var(--dusk-orange) 100%);
  }
  .quote-line {
    margin: 0;
    font-size: 20px;
    line-height: 29px;
    font-weight: 400;
    white-space: nowrap;
  }
  .quote-line.emphasis {
    color: var(--accent-red);
    font-style: italic;
    font-weight: 500;
  }
  .quote-opening {
    position: absolute;
    left: 24px;
    top: 27px;
  }
  .quote-reflection {
    position: absolute;
    right: 34px;
    top: 268px;
    text-align: right;
  }
  .quote-reflection .lead-in {
    font-size: 26px;
    line-height: 33px;
  }
  .closing-question {
    position: absolute;
    left: 24px;
    top: 452px;
    margin: 0;
    color: var(--headline-white);
    font-weight: 800;
    font-style: italic;
    font-size: 36px;
    line-height: 42px;
    letter-spacing: 0.5px;
    text-transform: uppercase;
    text-shadow: 0 2px 6px rgba(0,0,0,0.35);
  }
</style>
</head>
<body>
  <main class="artwork">
    <div class="backdrop" role="img" aria-label="Sunset photograph of a hiker leaping between two rocky cliffs against a hazy blue sky with a bright orange sun below"></div>

    <section class="quote-opening">
      <p class="quote-line">The thing that's so interesting about being alive is that you're all in.</p>
      <p class="quote-line">No matter what you do, you're all in.</p>
      <p class="quote-line">This is gonna kill you, so I think you might as well play</p>
      <p class="quote-line">the most magnificent game you can while you're waiting.</p>
      <p class="quote-line emphasis">Because, do you have anything better to do?</p>
      <p class="quote-line">Why not pick the best thing possible that you could do?</p>
      <p class="quote-line emphasis">Because you're more powerful than you think,</p>
      <p class="quote-line">way more powerful than you think.</p>
    </section>

    <section class="quote-reflection">
      <p class="quote-line emphasis lead-in">I mean, God only knows</p>
      <p class="quote-line">what you are in the final analysis.</p>
      <p class="quote-line">You're blind to your own weaknesses,</p>
      <p class="quote-line">but you're also blind to your own strengths.</p>
      <p class="quote-line">How far could you take that</p>
      <p class="quote-line emphasis">if you stopped wasting time, and</p>
      <p class="quote-line emphasis">if you stopped lying, and</p>
      <p class="quote-line emphasis">if you oriented yourself to the highest possible good that</p>
      <p class="quote-line">you could conceive of and you committed to that?</p>
      <p class="quote-line">How much good could you do?</p>
    </section>

    <h1 class="closing-question">Well,<br>I would say :<br>Why don’t you find out?</h1>
  </main>
</body>
</html>
```